Poster

I need a poster for my business, www.brightharbortastingtours.com which some information about the most important activities (Sangria Tasting, Iberian Ham, Charcuteries & Sherry Wine Tasting, Sailboat Experiences and Picnic Experiences). A3 Format. Social media included (@brightharbortoursbht), contact information included.

```html
<!DOCTYPE html>
<html lang="en">
<head>
<meta charset="utf-8">
<title>Bright Harbor Tasting Tours – Poster</title>
<link href="https://fonts.googleapis.com/css2?family=Poppins:wght@400;500;600;700&family=Montserrat:wght@500;600;700&family=Pacifico&display=swap" rel="stylesheet">
<style>
:root{
  --stage:#141414;
  --orange:#f0a21a;
  --gold:#c8892a;
  --ink:#2f2f2f;
  --grey:#555a60;
  --paper:#f6f3ee;
  --blue:#1f5fb0;
  --white:#ffffff;
}
*{margin:0;padding:0;box-sizing:border-box}
html,body{width:1200px;height:1200px;overflow:hidden;background:var(--stage)}
.canvas{position:relative;width:1200px;height:1200px;font-family:"Poppins",sans-serif;color:var(--ink)}
.side-label{position:absolute;top:155px;font-family:"Montserrat",sans-serif;font-weight:600;font-size:25px;color:var(--white);letter-spacing:.5px}
.side-label.front{left:287px}
.side-label.back{left:844px}

/* front */
.front-page{position:absolute;left:51px;top:215px;width:542px;height:769px;background:var(--paper);overflow:hidden}
.brush-top{position:absolute;left:250px;top:0;width:292px;height:90px;background:linear-gradient(100deg,rgba(176,150,205,0) 0%,#b7a0d3 35%,#a98fcb 100%)}
.brand{position:absolute;left:28px;top:30px;display:flex;align-items:center;gap:12px}
.brand-mark{width:30px;height:30px;background:var(--orange)}
.brand-name{font-weight:600;font-size:22px;line-height:1.1;color:var(--grey);text-transform:uppercase}
.photo{position:absolute}
.town-photo{left:0;top:180px;width:350px;height:175px;background:linear-gradient(180deg,#3b3f63 0%,#8f6f7a 45%,#d9a35a 70%,#c9bcd6 100%);clip-path:polygon(0 12%,40% 0,100% 20%,100% 100%,8% 95%,0 80%)}
.chef-photo{left:298px;top:30px;width:270px;height:290px;border-radius:26px;border:5px solid var(--white);background:linear-gradient(160deg,#6b6152 0%,#a6927a 40%,#7fc8c6 60%,#2b2b2b 100%);transform:rotate(-12deg)}
.sea-wash{position:absolute;left:300px;top:330px;width:242px;height:130px;background:linear-gradient(180deg,#7cc3bd 0%,#bfe1d9 50%,rgba(246,243,238,0) 100%)}
.welcome{position:absolute;left:56px;top:338px;font-family:"Pacifico",cursive;font-size:82px;line-height:1.2;color:var(--gold);text-shadow:2px 2px 0 #fff,-2px -2px 0 #fff,2px -2px 0 #fff,-2px 2px 0 #fff;white-space:nowrap;transform:rotate(-4deg)}
.place-band{position:absolute;left:125px;top:440px;width:305px;height:38px;background:var(--blue);clip-path:polygon(3% 8%,100% 0,97% 100%,0 92%);display:flex;align-items:center;justify-content:center;font-family:"Montserrat",sans-serif;font-weight:700;font-size:20px;color:var(--white);letter-spacing:.3px}
.sunset-photo{left:30px;top:505px;width:180px;height:180px;border-radius:22px;border:5px solid var(--white);background:linear-gradient(180deg,#e3a98f 0%,#b67c8f 40%,#4b3a5c 70%,#2a2238 100%);transform:rotate(-8deg)}
.sunset-splash{position:absolute;left:14px;top:502px;width:70px;height:30px;background:var(--gold);border-radius:40% 60% 30% 70%}
.intro{position:absolute;left:230px;top:518px;width:285px;font-size:12.3px;line-height:15.9px;color:#333}
.front-footer{position:absolute;left:0;bottom:0;width:542px;height:70px;background:var(--orange)}
.wave{position:absolute;left:0;top:-6px}
.contact-lines{position:absolute;left:30px;top:18px;font-size:10.6px;line-height:17px;color:#2b2b2b}
.contact-lines div{display:flex;align-items:center;gap:5px}
.contact-lines .web{font-weight:600}
.footer-divider{position:absolute;left:309px;top:16px;width:2px;height:40px;background:#2b2b2b}
.phone{position:absolute;left:329px;top:20px;display:flex;align-items:center;gap:7px;font-weight:700;font-size:18.5px;color:#2b2b2b}

/* back */
.back-page{position:absolute;left:607px;top:215px;width:544px;height:769px;background:linear-gradient(160deg,#f3f4f7 0%,#e6e8ee 60%,#eceef3 100%);overflow:hidden}
.back-strip{position:absolute;left:0;top:0;width:158px;height:769px;background:var(--orange)}
.gallery{position:absolute;left:28px;top:23px;width:178px}
.gallery-item{width:178px;height:163px;background:var(--white);border-radius:10px;padding:6px;margin-bottom:7px;box-shadow:0 1px 4px rgba(0,0,0,.08)}
.gallery-item div{width:100%;height:100%;border-radius:4px}
.g-sangria{background:linear-gradient(180deg,#6a7fa6 0%,#c9ccd6 40%,#5b3f8a 75%,#3d2a66 100%)}
.g-ham{background:linear-gradient(180deg,#7a6a58 0%,#2e2a28 45%,#1f1c1b 100%)}
.g-sail{background:linear-gradient(180deg,#c9c3b5 0%,#8ea0b3 50%,#1f3d66 100%)}
.g-picnic{background:linear-gradient(180deg,#7ba0c4 0%,#c9a67a 45%,#e8e4de 100%)}
.offers{position:absolute;left:231px;top:26px;width:290px;color:var(--grey)}
.group{margin-bottom:13px}
.offer-title{font-weight:600;font-size:16.2px;line-height:19.5px;color:#3b3b3b;margin-bottom:5px}
.offer-sub{position:relative;padding-left:12px;font-weight:500;font-size:12.8px;line-height:16px;color:#3b3b3b;margin-bottom:2px;white-space:nowrap}
.offer-sub::before{content:"";position:absolute;left:1px;top:6px;width:6px;height:6px;border-radius:50%;background:var(--orange)}
.offer-text{font-size:10.6px;line-height:12.9px;letter-spacing:.2px;text-align:justify;margin-bottom:8px}
.offer-text:last-child{margin-bottom:0}
.offer-text.indented{padding-left:12px}
.offer-text b{font-weight:600;color:#2f2f2f}
.socials{position:absolute;left:177px;top:719px;display:flex;gap:5px}
.socials span{width:28px;height:28px;border-radius:50%;border:1px dashed #888;background:var(--white)}
.handle{position:absolute;left:284px;top:715px;width:240px;height:33px;border-radius:17px;background:var(--orange);display:flex;align-items:center;justify-content:center;font-weight:500;font-size:15.5px;color:#2b2b2b}
</style>
</head>
<body>
<div class="canvas">
  <div class="side-label front">Front</div>
  <div class="side-label back">Back</div>

  <section class="front-page">
    <div class="brush-top"></div>
    <div class="brand">
      <span class="brand-mark"></span>
      <div class="brand-name">Bright Harbor<br>Tasting Tours</div>
    </div>
    <div class="photo town-photo" role="img" aria-label="Coastal town with lit apartment buildings at dusk"></div>
    <div class="sea-wash"></div>
    <div class="photo chef-photo" role="img" aria-label="Host in an apron cooking paella in front of wine shelves"></div>
    <div class="welcome">Welcome to</div>
    <div class="place-band">MARBELLA &amp; ESTEPONA</div>
    <div class="sunset-splash"></div>
    <div class="photo sunset-photo" role="img" aria-label="Sunset over the sea with waves"></div>
    <p class="intro">Elevate your taste buds with our gastronomic experiences boasting breathtaking views of Marbella &amp; Estepona! Dive into a world of culinary delights set against a backdrop of awe-inspiring beauty. From mouthwatering dishes to panoramic vistas, it’s the ultimate choice for foodies seeking an unforgettable experience. Join us and treat yourself to the best of Marbella &amp; Estepona’s flavors with a side of stunning scenery.</p>
    <footer class="front-footer">
      <svg class="wave" width="542" height="8" viewBox="0 0 542 8" preserveAspectRatio="none"><path d="M0 8 Q4.5 0 9 8 T18 8 T27 8 T36 8 T45 8 T54 8 T63 8 T72 8 T81 8 T90 8 T99 8 T108 8 T117 8 T126 8 T135 8 T144 8 T153 8 T162 8 T171 8 T180 8 T189 8 T198 8 T207 8 T216 8 T225 8 T234 8 T243 8 T252 8 T261 8 T270 8 T279 8 T288 8 T297 8 T306 8 T315 8 T324 8 T333 8 T342 8 T351 8 T360 8 T369 8 T378 8 T387 8 T396 8 T405 8 T414 8 T423 8 T432 8 T441 8 T450 8 T459 8 T468 8 T477 8 T486 8 T495 8 T504 8 T513 8 T522 8 T531 8 T540 8 L542 8Z" fill="#f0a21a"/></svg>
      <div class="contact-lines">
        <div><svg width="14" height="11" viewBox="0 0 14 11"><rect x="1" y="1" width="12" height="9" fill="none" stroke="#2b2b2b" stroke-width="1.2"/><path d="M1 1 L7 6 L13 1" fill="none" stroke="#2b2b2b" stroke-width="1.2"/></svg>info@brightharbortastingtours.com</div>
        <div class="web"><svg width="13" height="13" viewBox="0 0 13 13"><circle cx="6.5" cy="6.5" r="5.5" fill="none" stroke="#2b2b2b" stroke-width="1.2"/><ellipse cx="6.5" cy="6.5" rx="2.5" ry="5.5" fill="none" stroke="#2b2b2b" stroke-width="1"/><line x1="1" y1="6.5" x2="12" y2="6.5" stroke="#2b2b2b" stroke-width="1"/></svg>www.brightharbortastingtours.com</div>
      </div>
      <div class="footer-divider"></div>
      <div class="phone"><svg width="24" height="24" viewBox="0 0 24 24"><circle cx="12" cy="12" r="10.5" fill="none" stroke="#2b2b2b" stroke-width="1.8"/><path d="M8.5 7 L10.5 7 L11.2 9.6 L10 10.6 Q11 13 13.4 14 L14.4 12.8 L17 13.5 L17 15.5 Q16.5 17 14.5 16.8 Q9 15.5 7.2 9.5 Q7 7.5 8.5 7Z" fill="#2b2b2b"/></svg>+34 600 123 456</div>
    </footer>
  </section>

  <section class="back-page">
    <div class="back-strip"></div>
    <div class="gallery">
      <div class="gallery-item"><div class="g-sangria" role="img" aria-label="Glasses of sangria on a terrace table at dusk"></div></div>
      <div class="gallery-item"><div class="g-ham" role="img" aria-label="Bowl of olives and a board of cured meats"></div></div>
      <div class="gallery-item"><div class="g-sail" role="img" aria-label="Sailboat on the open sea"></div></div>
      <div class="gallery-item"><div class="g-picnic" role="img" aria-label="Picnic basket with bread, cheese and pastries by the sea"></div></div>
    </div>

    <div class="offers">
      <div class="group">
        <h2 class="offer-title">Sangria Tasting</h2>
        <p class="offer-text">During this experience, you will try four distinct types of authentic Sangria, each crafted with different wines and fresh, locally sourced ingredients.</p>
      </div>

      <div class="group">
        <h2 class="offer-title">Iberian Ham, Charcuteries &amp;<br>Sherry Wine Tasting</h2>
        <p class="offer-text">Indulge in the rich flavors of Spain with our Iberian Charcuteries &amp; Sherry Wine Tasting. Sample two premium Iberian hams, three distinct sausages, and a variety of olives, all perfectly paired with a selection of Sherry wines. Learn about the intricate production processes behind these gourmet products from a knowledgeable expert. This immersive experience is perfect for food enthusiasts looking to explore the essence of Iberian cuisine and the complexities of Sherry wine.</p>
      </div>

      <div class="group">
        <h2 class="offer-title">Sailboat Experiences</h2>
        <h3 class="offer-sub">Sailboat Sangria Tasting Experience</h3>
        <p class="offer-text indented">The Sailboat Sangria Tasting Experience is a unique and enchanting journey where you can relax and unwind while sailing along the beautiful coast of Estepona.<br><b>Join us for this unique 2 hour experience!</b></p>
        <h3 class="offer-sub">Sailboat Cheese &amp; Wine Picnic Experience</h3>
        <p class="offer-text indented">The Sailboat Cheese &amp; Wine Picnic Experience is a unique and elegant journey where you can relax and unwind while sailing along the beautiful coast of Estepona.<br><b>Join us for this unique 2 hour experience!</b></p>
      </div>

      <div class="group">
        <h2 class="offer-title">Picnic Experiences</h2>
        <h3 class="offer-sub">Picnic Brunch Experience</h3>
        <p class="offer-text indented">Indulge in a unique morning retreat with our Picnic Brunch Experience from Estepona to Sunset Cove. Select from our gourmet picnic basket filled with freshly baked pastries, artisanal cheeses, cured meats, seasonal fruits, and decadent desserts.</p>
        <h3 class="offer-sub">Picnic Tapas Experience</h3>
        <p class="offer-text indented">Indulge in a unique outdoor dining adventure with our Picnic Tapas Experience. Savor an array of traditional Spanish tapas and elevate your seaside escapade with a personalized picnic spread.</p>
      </div>
    </div>

    <div class="socials"><span></span><span></span><span></span></div>
    <div class="handle">@brightharbortoursbht</div>
  </section>
</div>
</body>
</html>
```